Talbrin Business Cards

Front and back. Simon Kavelle MBA is the CEO of Talbrin Homes. Black white and grays. Logo and cool design.

Target Market(s)

Professional lenders and investors

Industry/Entity Type

Real estate developer. NO HOUSES OR ROOFS

Contact Information for Business Card

Logo, name and unique design. Front and back. Simon Kavelle MBA is the CEO of Talbrin Homes. Black white and grays. Logo and cool design.

Font styles to use
Sans Serif

Colors

Designer to choose only greyscale colors for use in the design.

Requirements
Must have
• Cool look. Not the same card I could design.
Nice to have
• Something memorable
Should not have
• Basic

```html
<!DOCTYPE html>
<html lang="en">
<head>
<meta charset="utf-8">
<title>Talbrin Homes – Business Cards</title>
<link href="https://fonts.googleapis.com/css2?family=Montserrat:wght@300;400;700;800&display=swap" rel="stylesheet">
<style>
  :root {
    --backdrop: #d6d6d6;
    --paper: #ffffff;
    --ink: #0b0b0b;
    --ink-soft: #2a2a2a;
    --line-grey: #bdbdbd;
    --pattern-light: #f4f4f4;
    --pattern-dark: #c9c9c9;
  }
  * { box-sizing: border-box; margin: 0; padding: 0; }
  html, body {
    width: 1200px; height: 846px; overflow: hidden;
    background: var(--backdrop);
    font-family: "Montserrat", sans-serif;
  }
  .sheet {
    position: relative; width: 1200px; height: 846px;
    display: flex; align-items: center; justify-content: center; gap: 60px;
  }
  .card {
    position: relative; width: 520px; height: 297px; overflow: hidden;
    box-shadow: 0 10px 28px rgba(0,0,0,0.18);
  }
  /* Front */
  .card--front { background: var(--paper); color: var(--ink); }
  .front__pattern {
    position: absolute; right: 0; top: 0; width: 240px; height: 297px;
    background: linear-gradient(200deg, var(--pattern-dark) 0%, var(--pattern-light) 55%, var(--paper) 80%);
    clip-path: polygon(30% 0, 100% 0, 100% 100%, 70% 100%, 55% 62%, 80% 48%, 48% 30%, 10% 22%);
  }
  .front__brand {
    position: absolute; left: 34px; top: 120px; width: 150px;
    text-align: center;
  }
  .brand-name {
    font-weight: 800; font-size: 30px; letter-spacing: -0.5px; line-height: 1;
  }
  .brand-sub {
    display: block; font-weight: 800; font-size: 11px; letter-spacing: 6px; margin-top: 6px;
  }
  .front__divider {
    position: absolute; left: 200px; top: 60px; width: 1px; height: 180px;
    background: var(--ink);
  }
  .front__details { position: absolute; left: 222px; top: 62px; }
  .person__name { font-weight: 800; font-size: 20px; line-height: 1.15; }
  .person__title { font-weight: 700; font-size: 14px; margin-top: 2px; }
  .contacts { list-style: none; margin-top: 24px; }
  .contacts li {
    display: flex; align-items: center; gap: 9px;
    font-weight: 300; font-size: 13px; line-height: 1; height: 22px;
  }
  .contacts svg { width: 13px; height: 13px; flex: none; fill: var(--ink); }
  /* Back */
  .card--back {
    background: var(--ink); color: var(--paper);
    display: flex; flex-direction: column; align-items: center; justify-content: center;
  }
  .back__name { font-weight: 800; font-size: 86px; letter-spacing: -2px; line-height: 0.9; }
  .back__sub { font-weight: 300; font-size: 16px; letter-spacing: 12px; margin-top: 10px; padding-left: 12px; }
</style>
</head>
<body>
<main class="sheet">
  <section class="card card--front" aria-label="Card front">
    <div class="front__pattern" role="img" aria-label="Architectural line drawing of stepped building forms"></div>
    <div class="front__brand">
      <span class="brand-name">Talbrin</span>
      <span class="brand-sub">HOMES</span>
    </div>
    <div class="front__divider"></div>
    <div class="front__details">
      <p class="person__name">Simon Kavelle</p>
      <p class="person__title">MBA CEO</p>
      <ul class="contacts">
        <li><svg viewBox="0 0 16 16" aria-hidden="true"><path d="M4 1l3 3-1.8 1.8a9 9 0 0 0 5 5L12 9l3 3-2 2.5C7 14 2 9 1.5 3z"/></svg>1-555-014-2270</li>
        <li><svg viewBox="0 0 16 16" aria-hidden="true"><path d="M1 3h14v10H1z M1 3l7 6 7-6" /></svg>simon@talbrinhomes.com</li>
        <li><svg viewBox="0 0 16 16" aria-hidden="true"><circle cx="8" cy="8" r="6"/></svg>social/TalbrinHomes</li>
        <li><svg viewBox="0 0 16 16" aria-hidden="true"><circle cx="8" cy="8" r="7"/><path d="M1 8h14M8 1v14" stroke="#fff" stroke-width="1.2" fill="none"/></svg>www.talbrinhomes.com</li>
      </ul>
    </div>
  </section>

  <section class="card card--back" aria-label="Card back">
    <p class="back__name">Talbrin</p>
    <p class="back__sub">HOMES</p>
  </section>
</main>
</body>
</html>
```